High end personal training flyer design

I want a flyer designed to be delivered to people's houses to interest them in high end (and, therefore, not cheap) personal training services.

Don't want standard pictures of people exercising, before and afters, etc. More something that will appeal to that more affluent market.

Flexible on size of flyer, but please make sure it is a standard size that I can get printed easily. Would like it not to look like a normal flyer you get through the letterbox, so if any particular sizes, shapes, etc are known to do that, then that would be a good start.

Text on flyer to be as follows:

Is this you:

Live in East Cheshire
Male, aged 30-50
A father
Cash rich, time poor
Find handling high pressure at work comfortable
But have a short fuse out of work – with the wife, kids, life in general, etc
Not happy with the way your body looks and feels
Know exactly what you should do to sort that, but struggling to actually do it for various reasons
Turned off by the standard menu of options for addressing that – gyms, slimming clubs, diets, etc

If so, you may be interested in what I do.

Some would call it Personal Training. Some would call it Coaching. I’m not interested in giving what I do labels.

What I am interested in is providing the best possible service (and results) for my clients – whatever that entails.

I work closely with one or two clients at a time to make sure they get exactly what they need.

If you would like to find out more about this, I usually meet for a coffee and a chat. To see if we both think our working together is a good idea.

No squeeze pages, no countdowns, mailing lists or false scarcity.

No plastering this flyer with ‘Before and afters’ – they are ten a penny and my clients don’t want to have pictures of them in their underwear spread around the local area.

Just give me a call and we’ll go from there.

My number is 07912645320.

Tim

Industry/Entity Type

Training

Requirements
Should not have
• Generic before and after or exercise type pictures

```html
<!DOCTYPE html>
<html lang="en">
<head>
<meta charset="utf-8">
<title>Tim – Flyer</title>
<link rel="stylesheet" href="https://fonts.googleapis.com/css2?family=Arimo:wght@400;700&family=Bebas+Neue&family=Oswald:wght@400&display=swap">
<style>
  :root {
    --ink: #000000;
    --teal: #073f46;
    --orange: #e07b1f;
    --white: #ffffff;
    --rule: #ffffff;
  }
  * { margin: 0; padding: 0; box-sizing: border-box; }
  html, body { width: 849px; height: 1200px; overflow: hidden; background: #ffffff; }
  .flyer {
    position: relative;
    width: 849px;
    height: 1200px;
    overflow: hidden;
    background: linear-gradient(180deg, var(--ink) 0%, #050a0c 40%, #0a2427 70%, var(--teal) 100%);
    color: var(--white);
    font-family: "Arimo", Arial, sans-serif;
  }
  .headline {
    position: absolute;
    top: 4px; left: 0; width: 100%;
    text-align: center;
    font-family: "Bebas Neue", sans-serif;
    font-size: 118px;
    line-height: 1;
  }
  .accent { color: var(--orange); }
  .hero-photo {
    position: absolute;
    top: 108px; left: 0;
    width: 100%; height: 364px;
    background: radial-gradient(ellipse 38% 55% at 50% 55%, #6b3a22 0%, #3a1e12 45%, #0a0605 80%, transparent 100%);
  }
  .rule {
    position: absolute;
    left: 24px; width: 801px; height: 3px;
    background: var(--rule);
  }
  .profile {
    position: absolute;
    top: 485px; left: 0; width: 100%;
    text-align: center;
    font-size: 18.5px;
    line-height: 22px;
    white-space: nowrap;
  }
  .profile .strong { font-weight: 700; }
  .profile .pain {
    color: var(--orange);
    font-weight: 700;
    font-size: 27px;
    line-height: 32px;
  }
  .quote { display: inline-block; vertical-align: top; margin: 2px 3px 0; }
  .wordmark-line { position: absolute; left: 0; width: 100%; }
  .pitch {
    position: absolute;
    top: 913px; left: 0; width: 849px;
    text-align: center;
    font-size: 16.2px;
    line-height: 19.6px;
    white-space: nowrap;
  }
  .signature {
    position: absolute;
    left: 40px; top: 1068px;
    display: flex;
    align-items: center;
    gap: 16px;
  }
  .signature-dot {
    width: 56px; height: 56px;
    border-radius: 50%;
    background: var(--orange);
  }
  .signature-name {
    font-family: "Bebas Neue", sans-serif;
    font-size: 76px;
    line-height: 1;
    color: var(--white);
    padding-top: 6px;
  }
  .call-line { position: absolute; top: 1036px; left: 279px; }
  .phone { position: absolute; top: 1070px; left: 279px; }
</style>
</head>
<body>
<main class="flyer">
  <h1 class="headline">Is this <span class="accent">you</span></h1>

  <div class="hero-photo" role="img" aria-label="Photo of a man and a woman lifting dumbbells against a dark background"></div>

  <div class="rule" style="top:471px"></div>

  <section class="profile">
    <p class="strong"><svg class="quote" width="14" height="16" viewBox="0 0 14 16"><rect x="0" y="1" width="5" height="13" rx="2" fill="var(--orange)"/><rect x="7" y="1" width="5" height="13" rx="2" fill="var(--orange)"/></svg>Live in East Cheshire<svg class="quote" width="14" height="16" viewBox="0 0 14 16"><rect x="0" y="1" width="5" height="13" rx="2" fill="var(--orange)"/><rect x="7" y="1" width="5" height="13" rx="2" fill="var(--orange)"/></svg></p>
    <p class="strong">Male, aged 30-50</p>
    <p>A father</p>
    <p>Cash rich, time poor</p>
    <p>Find handling high pressure at work comfortable</p>
    <p>But have a short fuse out of work – with the wife, kids, life in general, etc</p>
    <p class="pain"><svg class="quote" width="14" height="16" viewBox="0 0 14 16"><rect x="0" y="1" width="5" height="13" rx="2" fill="var(--orange)"/><rect x="7" y="1" width="5" height="13" rx="2" fill="var(--orange)"/></svg>Not happy with the way your body looks and feels<svg class="quote" width="14" height="16" viewBox="0 0 14 16"><rect x="0" y="1" width="5" height="13" rx="2" fill="var(--orange)"/><rect x="7" y="1" width="5" height="13" rx="2" fill="var(--orange)"/></svg></p>
    <p>Know exactly what you should do to sort that, but struggling to actually do it for various reasons</p>
    <p>Turned off by the standard menu of options for addressing that – gyms, slimming clubs, diets, etc</p>
  </section>

  <div class="rule" style="top:713px"></div>

  <svg class="wordmark-line" style="top:726px" width="849" height="40" viewBox="0 0 849 40">
    <text x="24" y="35" textLength="801" lengthAdjust="spacingAndGlyphs" font-family="Bebas Neue, sans-serif" font-size="41" fill="var(--white)">NO SQUEEZE PAGES <tspan fill="var(--orange)">/</tspan> NO COUNTDOWNS <tspan fill="var(--orange)">/</tspan> MAILING LISTS <tspan fill="var(--orange)">OR</tspan> FALSE SCARCITY.</text>
  </svg>

  <svg class="wordmark-line" style="top:770px" width="849" height="125" viewBox="0 0 849 125">
    <text x="97" y="120" textLength="653" lengthAdjust="spacingAndGlyphs" font-family="Bebas Neue, sans-serif" font-size="157" fill="var(--white)">JUST <tspan fill="var(--orange)">RESULTS</tspan></text>
  </svg>

  <p class="pitch">Some would call it Personal Training. Some would call it Coaching. I’m not interested in giving what I do labels.<br>What I am interested in is providing the best possible service (and results) for my clients –whatever that entails.<br>I work closely with one or two clients at a time to make sure they get exactly what they need.If you would like to<br>find out more about this, I usually meet for a coffee and a chat.To see if we both think our working together is a<br>good idea.</p>

  <div class="rule" style="top:1021px"></div>

  <div class="signature">
    <span class="signature-dot"></span>
    <span class="signature-name">TIM</span>
  </div>

  <svg class="call-line" width="490" height="40" viewBox="0 0 490 40">
    <text x="0" y="34" textLength="489" lengthAdjust="spacingAndGlyphs" font-family="Bebas Neue, sans-serif" font-size="36" fill="var(--orange)">JUST GIVE ME A CALL AND WE’LL GO FROM THERE</text>
  </svg>

  <svg class="phone" width="490" height="95" viewBox="0 0 490 95">
    <text x="0" y="91" textLength="488" lengthAdjust="spacingAndGlyphs" font-family="Oswald, sans-serif" font-weight="400" font-size="108" fill="var(--white)">07912645320</text>
  </svg>
</main>
</body>
</html>
```